Ordinary Velvet Sparrow inquiring into the Mystery of her Heart needs a Book Cover design

Hello! I need a book cover design (for printed softcover 6” x 9” and eBook) for my new book titled "The Wide Season of a Modest Velvet Sparrow: Notes on Finding Room for Every Part." It's the story of a mom juggling a demanding technology career who embarks upon a self-discovery journey, faces cancer, and learns to expand her life, one vulnerable nibble at a time. With the help of a guide on her spiritual path, she learns to let go of her strong woman do-it-all persona, allowing her soul to fully shine. My purpose in writing the book is to share what I've learned about finding the "moreness" in being human.
*I would like to see book cover designs that communicate a sense of both strength and vulnerability, confidence and humbleness, curiosity and inner discovery—hinting at what's to come. I’ve uploaded a few images that I like because they feel clean and simple, and because they can be interpreted as metaphors of the beauty and power within each of us.
*If your design submission includes a mirror reflection of some sort of a “velvet sparrow” image that people are familiar with, then I would like it to convey a reluctant or questioning velvet sparrow, rather than a bold, fighting-to-save-the-world velvet sparrow.
*I lean toward a clean and calming background, as the book is really an inquiry into the mystery of this heart. It’s an examination of what I might have lost of myself, and ultimately gained, through all my crazy years of juggling. So, it’s a journey of spiritual growth.
Thank you for your interest and sharing your creative talent.

Target Market(s)

(1) Career-oriented parents, especially moms, who are in their 30's and 40's, in the midst of the struggle of trying to juggle it all; (2) life-long strivers, age 55+, who are finally slowing down and looking back to try and make sense of their lives, seeking to understand their buried inner life

Industry/Entity Type

Book Categories: Women & Business; Spiritual Self-help; Strong Women

Font styles to use
Serif

Colors

Designer to choose colors to be used in the design.

Requirements
Must have
• Clean and simple overall feeling
Nice to have
• I am open to including color—if so, perhaps some (not too much) hunter green would be nice (not required, but I’ve used it in a draft website design and rather like it).
Should not have
• Should not feel too "busy"

```html
<!DOCTYPE html>
<html lang="en">
<head>
<meta charset="utf-8">
<title>The Wide Season of a Modest Velvet Sparrow – Book Cover</title>
<link rel="stylesheet" href="https://fonts.googleapis.com/css2?family=Playfair+Display:ital,wght@0,600;1,400&family=Cormorant+Garamond:wght@600&display=swap">
<style>
  :root {
    --stage: #000000;
    --paper-top: #f8f7f5;
    --paper-bottom: #eeecea;
    --teal: #1fa89b;
    --mauve: #9a8ea7;
    --ink: #1c1c1c;
    --author-grey: #a3a3a3;
    --art-lilac: #c9b8d6;
    --art-mint: #9fd3c7;
    --art-blush: #eab2a8;
  }
  html, body {
    margin: 0;
    padding: 0;
    width: 1200px;
    height: 1200px;
    overflow: hidden;
    background: var(--stage);
  }
  .stage {
    position: relative;
    width: 1200px;
    height: 1200px;
    background: var(--stage);
  }
  .cover {
    position: absolute;
    left: 242px;
    top: 63px;
    width: 716px;
    height: 1079px;
    background: linear-gradient(180deg, var(--paper-top) 0%, var(--paper-top) 55%, var(--paper-bottom) 100%);
    overflow: hidden;
  }
  .title {
    position: absolute;
    left: 0;
    top: 0;
    width: 716px;
    height: 580px;
  }
  .title text {
    font-family: "Playfair Display", "Times New Roman", serif;
    font-weight: 600;
  }
  .title .teal { fill: var(--teal); }
  .title .mauve { fill: var(--mauve); }
  .title .rule { stroke: var(--teal); stroke-width: 2; }
  .subtitle {
    position: absolute;
    left: 0;
    top: 570px;
    width: 716px;
    margin: 0;
    text-align: center;
    font-family: "Playfair Display", "Times New Roman", serif;
    font-style: italic;
    font-weight: 400;
    font-size: 25px;
    color: var(--ink);
  }
  .cover-art {
    position: absolute;
    left: 205px;
    top: 595px;
    width: 310px;
    height: 370px;
    border-radius: 50%;
    background:
      radial-gradient(circle at 35% 30%, var(--art-mint) 0%, rgba(159,211,199,0) 45%),
      radial-gradient(circle at 45% 75%, var(--art-blush) 0%, rgba(234,178,168,0) 40%),
      radial-gradient(ellipse at 50% 50%, var(--art-lilac) 0%, rgba(201,184,214,0.5) 45%, rgba(248,247,245,0) 70%);
  }
  .author {
    position: absolute;
    left: 0;
    top: 990px;
    width: 716px;
    margin: 0;
    text-align: center;
    font-family: "Cormorant Garamond", "Times New Roman", serif;
    font-weight: 600;
    font-size: 31px;
    letter-spacing: 0.3em;
    text-indent: 0.3em;
    color: var(--author-grey);
  }
</style>
</head>
<body>
  <main class="stage">
    <article class="cover">
      <svg class="title" viewBox="0 0 716 580" aria-labelledby="book-title">
        <title id="book-title">The Wide Season of a Modest Velvet Sparrow</title>
        <line class="rule" x1="138" y1="50" x2="216" y2="50"/>
        <line class="rule" x1="478" y1="50" x2="555" y2="50"/>
        <text class="teal" x="358" y="115" text-anchor="middle" font-size="58" textLength="112" lengthAdjust="spacingAndGlyphs">THE</text>
        <text class="teal" x="358" y="212" text-anchor="middle" font-size="88" textLength="538" lengthAdjust="spacingAndGlyphs">WIDE SEASON</text>
        <text class="teal" x="358" y="284" text-anchor="middle" font-size="56" textLength="538" lengthAdjust="spacingAndGlyphs">OF A MODEST</text>
        <text class="mauve" x="358" y="387" text-anchor="middle" font-size="97" textLength="494" lengthAdjust="spacingAndGlyphs">VELVET</text>
        <text class="mauve" x="358" y="490" text-anchor="middle" font-size="97" textLength="544" lengthAdjust="spacingAndGlyphs">SPARROW</text>
      </svg>
      <p class="subtitle">Notes on Finding Room for Every Part</p>
      <div class="cover-art" role="img" aria-label="Paper-craft illustration of a woman's profile crowned with leaves, flowers and butterflies in lilac, mint and blush tones"></div>
      <p class="author">AUTHOR NAME</p>
    </article>
  </main>
</body>
</html>
```